Business Card Design for Kidlarko (Hires out childrens play areas)

Looking to have a business card designed for a company we just bought. The company rents out childrens play areas.

I have uploaded a couple of examples of the kind of business card style I like. Here are two more examples:

https://vesterlingstudio.example.nz/project/brisk-romp-branding/
https://imgvaultcdn.example.com/design_img/8462913/307481/307481_2958174_8462913_a7c3e190_image.jpg

I think a white card will be best due to all the colours in the logo.

Size we require: 3.75" x 2.25" (horizontally orientated) with a 0.125" bleed

Uploaded is two versions of our logo.

Details for the card:
1. My name: Wade Ferrin
2. Title: Managing Director
3. Phone no: 021 537 462
4. Email: wade@kidlarko.example.nz
5. URL: www.kidlarko.example.nz
6. Address:
PO Box 381627
Fernmoor, Auckland

Let me know if you need anything else.

Target Market(s)

Hospitals, doctors surgeries, bed shops, etc.

Contact Information for Business Card

Details for the card:
1. My name: Wade Ferrin
3. Phone no: 021 537 462
5. URL: www.kidlarko.example.nz
6. Address:
PO Box 381627
Fernmoor, Auckland

Requirements
Should not have
• Not too busy.

```html
<!DOCTYPE html>
<html lang="en">
<head>
<meta charset="utf-8">
<title>Kidlarko – Business Card</title>
<link rel="stylesheet" href="https://fonts.googleapis.com/css2?family=Quicksand:wght@500;700&display=swap">
<style>
  :root {
    --backdrop: #ebe6df;
    --card: #ffffff;
    --ink: #1f1f1f;
    --brand-blue: #1b5fae;
    --accent-orange: #f26522;
    --accent-purple: #a3268f;
    --icon-green: #2fa84f;
  }
  * { box-sizing: border-box; margin: 0; padding: 0; }
  html, body {
    width: 1200px; height: 1200px; overflow: hidden;
    background: var(--backdrop);
    font-family: "Quicksand", sans-serif;
    color: var(--ink);
  }
  .canvas { position: relative; width: 1200px; height: 1200px; }
  .card {
    position: absolute; left: 240px; width: 720px; height: 412px;
    background: var(--card); border-radius: 36px;
    box-shadow: 0 6px 18px rgba(0,0,0,.12);
  }
  .card--front { top: 146px; }
  .card--back { top: 643px; }

  .brand {
    position: absolute; display: flex; align-items: center; gap: 14px;
    color: var(--brand-blue); font-weight: 700; white-space: nowrap;
  }
  .brand__dot {
    width: 0.7em; height: 0.7em; border-radius: 50%;
    background: var(--accent-orange); flex: none;
  }
  .card--front .brand {
    left: 0; right: 0; top: 170px; justify-content: center; font-size: 78px; line-height: 1;
  }
  .card--back .brand {
    left: 380px; top: 190px; font-size: 44px; line-height: 1;
  }

  .details { position: absolute; right: 397px; top: 108px; text-align: right; }
  .group { position: relative; }
  .group::after {
    content: ""; position: absolute; right: -21px; width: 2px;
    background: var(--brand-blue);
  }
  .group--name::after { top: 2px; height: 44px; }
  .group--address { margin-top: 12px; }
  .group--address::after { top: 4px; height: 40px; background: var(--accent-purple); }
  .group--contact { margin-top: 16px; }
  .group--contact::after { top: 4px; height: 76px; }

  .person__name {
    color: var(--accent-orange); font-weight: 700; font-size: 27px;
    letter-spacing: .5px; line-height: 1;
  }
  .person__title, .address__line { font-size: 19px; font-weight: 500; line-height: 24px; }
  .person__title { margin-top: 3px; }

  .contact__line {
    font-size: 18.5px; font-weight: 500; line-height: 29px;
    display: flex; justify-content: flex-end; align-items: center; gap: 11px;
  }
  .contact__icon { width: 16px; height: 16px; flex: none; }
</style>
</head>
<body>
<main class="canvas">
  <section class="card card--front" aria-label="Card front">
    <div class="brand"><span class="brand__dot"></span>Kidlarko</div>
  </section>

  <section class="card card--back" aria-label="Card back">
    <div class="details">
      <div class="group group--name">
        <p class="person__name">WADE FERRIN</p>
        <p class="person__title">Managing Director</p>
      </div>
      <div class="group group--address">
        <p class="address__line">PO Box 381627</p>
        <p class="address__line">Fernmoor, Auckland</p>
      </div>
      <div class="group group--contact">
        <p class="contact__line">021 537 462
          <svg class="contact__icon" viewBox="0 0 24 24" aria-hidden="true"><path fill="var(--icon-green)" d="M6.62 10.79c1.44 2.83 3.76 5.14 6.59 6.59l2.2-2.2c.27-.27.67-.36 1.02-.24 1.12.37 2.33.57 3.57.57.55 0 1 .45 1 1V20c0 .55-.45 1-1 1-9.39 0-17-7.61-17-17 0-.55.45-1 1-1h3.5c.55 0 1 .45 1 1 0 1.25.2 2.45.57 3.57.11.35.03.74-.25 1.02l-2.2 2.2z"/></svg>
        </p>
        <p class="contact__line">wade@kidlarko.example.nz
          <svg class="contact__icon" viewBox="0 0 24 24" aria-hidden="true"><rect x="2" y="5" width="20" height="14" rx="2" fill="var(--icon-green)"/><path d="M3 6.5l9 6.5 9-6.5" fill="none" stroke="#fff" stroke-width="1.8"/></svg>
        </p>
        <p class="contact__line">www.kidlarko.example.nz
          <svg class="contact__icon" viewBox="0 0 24 24" aria-hidden="true"><circle cx="12" cy="12" r="10" fill="var(--icon-green)"/><path d="M2 12h20M12 2c3 3 3 17 0 20M12 2c-3 3-3 17 0 20" fill="none" stroke="#fff" stroke-width="1.5"/></svg>
        </p>
      </div>
    </div>
    <div class="brand"><span class="brand__dot"></span>Kidlarko</div>
  </section>
</main>
</body>
</html>
```